Web form face-lift for an online startup

We are a web startup building a FreightDesk for the freight industry. The project is mainly dedicated to the paint the main form that our customer are using along the search results that the they get. All details are in the attached documents.
Updates
The application serves the Freight Forwarders community so please think towards this industry when using background images, banners, colors, icons, etc. Computer and technology images are irrelevant.
Customer fields at the top of the page is actually part of the form.
Target Market(s)
Usually business users (Sales people, procurement, shippers, freight forwarders). Some are less tech savvy and some appreciate the new trendy web apps.
Industry/Entity Type
Building
Colors
Designer to choose colors to be used in the design.
Look and feel
Each slider illustrates characteristics of the customer's brand and the style your logo design should communicate.

```html
<!DOCTYPE html>
<html lang="en">
<head>
<meta charset="utf-8">
<title>Search For Quotes</title>
<link href="https://fonts.googleapis.com/css2?family=Open+Sans:wght@400;600;700&display=swap" rel="stylesheet">
<style>
:root{
  --page-bg:#eaf4f3;
  --top-line:#1b6fa6;
  --brand-blue:#1b78b4;
  --nav-top:#1f94d2;
  --nav-bottom:#0b6fae;
  --nav-divider:#3aa6dc;
  --link:#1a6ea4;
  --text:#555b5e;
  --field-border:#c9cdcf;
  --panel-bg:#f6f6f6;
  --panel-border:#e0e2e3;
  --white:#ffffff;
  --heading:#4e8fb3;
}
*{box-sizing:border-box;margin:0;padding:0}
html,body{width:1072px;height:1200px;overflow:hidden;background:var(--page-bg)}
body{font-family:"Open Sans",Arial,sans-serif;color:var(--text);font-size:14px}
.stage{position:absolute;left:0;top:0;width:1000px;height:1119px;transform:scale(1.072);transform-origin:0 0;border-top:4px solid var(--top-line)}
.abs{position:absolute}

.brand{left:38px;top:29px;color:var(--brand-blue);font-weight:700;font-size:20px}
.utility{right:21px;top:30px;display:flex;gap:22px;font-size:14px;color:var(--link)}
.caret::after{content:"";display:inline-block;margin-left:4px;border:4px solid transparent;border-top-color:#9aa;border-bottom:0;vertical-align:middle}

.card{left:20px;top:84px;width:961px;height:983px;background:var(--white);border-radius:6px;box-shadow:0 1px 4px rgba(0,0,0,.3);overflow:hidden}
.main-nav{left:0;top:0;width:961px;height:40px;background:linear-gradient(var(--nav-top),var(--nav-bottom));display:flex}
.nav-home{width:42px;height:40px;display:flex;align-items:center;justify-content:center;border-right:1px solid var(--nav-divider)}
.nav-item{flex:1;color:var(--white);font-size:15px;display:flex;align-items:center;justify-content:center;border-right:1px solid var(--nav-divider)}
.nav-item:last-child{border-right:0}
.quick-links{left:0;top:40px;width:961px;height:39px;background:#f1f1f1;border-bottom:1px solid #d8d8d8;display:flex;align-items:center;gap:21px;padding-left:18px;font-size:13px}
.quick-links .ql-label{color:#a5a9ab}
.quick-links a{color:var(--link);font-weight:600;text-decoration:none}

.page-title{left:22px;top:136px;font-size:20px;font-weight:400;color:var(--heading);display:flex;align-items:center;gap:6px}
.label{color:var(--text);font-size:14px}
.field{position:absolute;background:var(--white);border:1px solid var(--field-border);height:29px;font-size:14px;color:var(--text);display:flex;align-items:center;padding-left:9px}
.field.center{justify-content:center;padding-left:0}
.select::after{content:"";position:absolute;right:9px;top:13px;border:4px solid transparent;border-top-color:#333;border-bottom:0}
.checkbox{position:absolute;width:11px;height:11px;border:1px solid #c3c3c3;background:#f4f4f4;border-radius:2px}
.radio{position:absolute;width:14px;height:14px;border:1px solid #b7b7b7;border-radius:50%;background:linear-gradient(#fff,#e7e7e7)}

.tab{position:absolute;top:256px;width:108px;height:58px;background:#f7f7f7;border:1px solid #e2e2e2;border-bottom:0;display:flex;align-items:center;justify-content:center}
.tab.active{background:var(--white);border-bottom:3px solid var(--brand-blue)}
.tab-art{width:44px;height:38px;border-radius:3px}
.btn{position:absolute;background:linear-gradient(#1e90cf,#0b6fad);color:var(--white);border-radius:3px;display:flex;align-items:center;justify-content:center;font-size:14px}

.panel{left:20px;top:314px;width:917px;height:576px;background:var(--panel-bg);border:1px solid var(--panel-border);border-radius:3px}
.rule{position:absolute;left:14px;width:885px;height:1px;background:#cfd2d3}
.link-strong{color:var(--link);font-weight:700}
.footer{left:0;top:926px;width:961px;height:57px;background:linear-gradient(#ffffff,#ececec);border-top:1px solid #e3e3e3}
.footer-links{position:absolute;top:20px;font-size:13px;color:#888;display:flex;gap:9px}
.footer-links a{color:var(--link);font-weight:600;text-decoration:none}
.copyright{left:0;width:1000px;top:1087px;text-align:center;font-size:13px;color:#666;font-weight:600}
</style>
</head>
<body>
<div class="stage">
  <div class="abs brand">FreightDesk</div>
  <div class="abs utility"><span class="caret">USD</span><span class="caret">English</span><span>Username</span></div>

  <main class="abs card">
    <nav class="abs main-nav">
      <div class="nav-home">
        <svg width="24" height="24" viewBox="0 0 24 24"><circle cx="12" cy="12" r="10" fill="none" stroke="#fff" stroke-width="2"/><path d="M12 12l5-5" stroke="#fff" stroke-width="2"/><circle cx="12" cy="12" r="1.8" fill="#fff"/></svg>
      </div>
      <div class="nav-item">Menu Item 1</div><div class="nav-item">Menu Item 2</div><div class="nav-item">Menu Item 3</div><div class="nav-item">Menu Item 4</div>
      <div class="nav-item">Menu Item 5</div><div class="nav-item">Menu Item 6</div><div class="nav-item">Menu Item 7</div><div class="nav-item">Menu Item 8</div>
    </nav>
    <div class="abs quick-links"><span class="ql-label">Quick Links :</span><a>SubLink 1</a><a>SubLink 1</a><a>SubLink 1</a><a>SubLink 1</a></div>

    <h1 class="abs page-title">
      <svg width="22" height="22" viewBox="0 0 22 22"><circle cx="8" cy="8" r="5.5" fill="none" stroke="#4e8fb3" stroke-width="2.5"/><path d="M12 12l7 7" stroke="#4e8fb3" stroke-width="3.5" stroke-linecap="round"/></svg>
      Search For Quotes
    </h1>
    <span class="abs label" style="left:22px;top:183px;font-weight:600">Customer</span>
    <div class="field" style="left:106px;top:178px;width:271px"></div>
    <span class="checkbox" style="left:107px;top:217px"></span>
    <span class="abs label" style="left:125px;top:213px;font-weight:600">Rate Quote ?</span>

    <div class="tab active" style="left:35px"><div class="tab-art" role="img" aria-label="Wooden crate with tools icon" style="background:linear-gradient(#f0b25a,#c9782e)"></div></div>
    <div class="tab" style="left:153px"><div class="tab-art" role="img" aria-label="Stacked red boxes on pallet icon" style="background:linear-gradient(#e0443b,#a8231c)"></div></div>
    <div class="tab" style="left:273px"><div class="tab-art" role="img" aria-label="Envelope with pencil icon" style="background:linear-gradient(#f4f4f4,#c8c8c8)"></div></div>
    <div class="btn" style="left:865px;top:271px;width:58px;height:29px">More</div>

    <section class="abs panel">
      <span class="abs label" style="left:28px;top:25px">Qty</span>
      <span class="abs label" style="left:85px;top:25px">Stacklabel</span>
      <span class="abs label" style="left:173px;top:25px">Load</span>
      <span class="abs label" style="left:469px;top:25px">Length</span>
      <span class="abs label" style="left:552px;top:25px">Width</span>
      <span class="abs label" style="left:635px;top:25px">Height</span>
      <span class="abs label" style="left:773px;top:25px">Weight</span>

      <div class="field center" style="left:15px;top:51px;width:49px">5</div>
      <span class="checkbox" style="left:109px;top:60px"></span>
      <div class="field select" style="left:173px;top:51px;width:271px">Box/ Pallet</div>
      <div class="field center" style="left:454px;top:51px;width:74px">100</div>
      <div class="field center" style="left:538px;top:51px;width:74px">100</div>
      <div class="field center" style="left:621px;top:51px;width:74px">100</div>
      <div class="field select" style="left:702px;top:51px;width:49px;padding-left:8px">cm</div>
      <div class="field center" style="left:759px;top:51px;width:74px">100</div>
      <div class="field select" style="left:841px;top:51px;width:49px;padding-left:11px">kg</div>

      <div class="btn" style="left:27px;top:112px;width:142px;height:31px;gap:5px"><span style="font-size:18px;font-weight:700;line-height:1">+</span>Add More Units</div>
      <div class="rule" style="top:162px"></div>

      <span class="abs label" style="left:478px;top:188px">Total</span>
      <div class="field center" style="left:524px;top:181px;width:74px">5</div>
      <div class="field center" style="left:604px;top:181px;width:74px">1</div>
      <div class="field select" style="left:677px;top:181px;width:74px;padding-left:10px">CBM</div>
      <div class="field center" style="left:759px;top:181px;width:74px">100</div>
      <div class="field select" style="left:841px;top:181px;width:49px;padding-left:11px">kg</div>
      <div class="rule" style="top:232px"></div>

      <span class="abs label" style="left:19px;top:263px">From</span>
      <div class="field" style="left:72px;top:258px;width:271px">Shipping address or port</div>
      <span class="abs label" style="left:592px;top:263px">To</span>
      <div class="field" style="left:625px;top:258px;width:271px">Shipping address or port</div>

      <span class="abs label" style="left:19px;top:334px;font-weight:600">OPTIONS</span>
      <span class="radio" style="left:30px;top:367px"></span><span class="abs label" style="left:52px;top:365px">Import</span>
      <span class="radio" style="left:112px;top:367px"></span><span class="abs label" style="left:134px;top:365px">Export</span>
      <span class="abs label" style="left:225px;top:365px">Incotem: FCA</span>
      <span class="checkbox" style="left:357px;top:368px"></span>
      <svg class="abs" style="left:373px;top:363px" width="20" height="20" viewBox="0 0 20 20"><circle cx="10" cy="10" r="8" fill="#3a78b8" stroke="#d0312d" stroke-width="2.4"/><path d="M4.5 4.5l11 11" stroke="#d0312d" stroke-width="2.4"/></svg>
      <span class="checkbox" style="left:410px;top:368px"></span>
      <svg class="abs" style="left:427px;top:363px" width="20" height="20" viewBox="0 0 20 20"><circle cx="10" cy="10" r="8" fill="#3a78b8" stroke="#d0312d" stroke-width="2.4"/><path d="M4.5 4.5l11 11" stroke="#d0312d" stroke-width="2.4"/></svg>
      <span class="checkbox" style="left:462px;top:368px"></span>
      <svg class="abs" style="left:479px;top:363px" width="20" height="20" viewBox="0 0 20 20"><circle cx="10" cy="10" r="8" fill="#fff" stroke="#d0312d" stroke-width="2.4"/><path d="M4.5 4.5l11 11" stroke="#d0312d" stroke-width="2.4"/></svg>
      <div class="field select" style="left:625px;top:361px;width:271px">Price Level</div>

      <span class="abs link-strong" style="left:807px;top:420px;font-size:13px">More Options</span>

      <div class="btn" style="left:358px;top:481px;width:201px;height:38px;font-size:17px;gap:8px;border-radius:1px">
        <svg width="24" height="24" viewBox="0 0 22 22"><circle cx="8" cy="8" r="5.5" fill="none" stroke="#fff" stroke-width="2.5"/><path d="M12 12l7 7" stroke="#fff" stroke-width="3.5" stroke-linecap="round"/></svg>
        Search Quotes
      </div>
      <span class="abs label" style="left:599px;top:490px">or</span>
      <span class="abs link-strong" style="left:628px;top:488px;font-size:15px">Create manually</span>
    </section>

    <footer class="abs footer">
      <div class="footer-links" style="left:25px"><a>About Us</a>|<a>Privacy Policy</a>|<a>Terms Of Service</a>|<a>News</a></div>
      <div class="footer-links" style="left:746px;top:23px"><a>Blog</a>|<a>Friendly</a>|<a>Chirper</a></div>
    </footer>
  </main>

  <p class="abs copyright">Copyright © 2014 - FreightDesk All Rights Reserved.</p>
</div>
</body>
</html>
```